Web Design Project for velbrook

We are looking for a sleek and sophisticated website design for our already developed web-based gallery management software application. Here is a link to our web-app: http://www.vel-brook.co

You will login on the main page and then we would like to include all of the information on the PDF that I am providing below (it outlines what?, where?, why? who? and how much?). Basically, we need a home page, about page, and a pricing page, as well as a sign up page that should be navigable from the upper right hand corner of the site where the sign in/sign up would be located. Also, our 3 tenets are that the software program is "attractive, accessible, and affordable", which might need to be somehow incorporated. There are a few websites that we would like for you to take inspiration from listed below:

https://tidemoxen.com (for homepage)
https://plumwovenly.com (for homepage/pricing page/etc)
https://tidemoxen.com/tour (for a tour of how the product works)

We are currently having a logo designed and will share that as soon as it is available! Also, let us know if you need photos/screen shots, as we can provide them.

Thanks!

Reason: Extending deadline as we are just now getting designs we would like to see fully developed.

Target Market(s)

art galleries, artists, art collectors, art consultants, museums

Industry/Entity Type

Software

Requirements
Must have
• Home page
About page (or tour through the app)
Pricing page
Sign up page (the more click-throughs to signing up the better)

```html
<!DOCTYPE html>
<html lang="en">
<head>
<meta charset="utf-8">
<title>velbrook — Gallery Management Made Easy</title>
<link rel="stylesheet" href="https://fonts.googleapis.com/css2?family=Roboto+Condensed:wght@400;700&display=swap">
<style>
  :root {
    --sky: #3ec3ee;
    --sky-light: #7fd9f7;
    --sky-deep: #1aa6d8;
    --nav-ink: #1d6a5c;
    --ink: #111111;
    --social-light: #38b3df;
    --social-dark: #0f6485;
    --paper: #ffffff;
    --panel: rgba(255, 255, 255, 0.5);
    --wall: #e9e5dc;
    --wall-shade: #c9c2b4;
    --ceiling: #4a463f;
    --floor: #2f2f2f;
  }
  * { box-sizing: border-box; margin: 0; padding: 0; }
  html, body { width: 1200px; height: 720px; overflow: hidden; background: var(--paper); }
  body { position: relative; font-family: "Roboto Condensed", "Arial Narrow", sans-serif; }

  .brand { position: absolute; left: 56px; top: 28px; display: flex; align-items: center; gap: 68px; text-decoration: none; }
  .brand-mark { width: 110px; height: 110px; border-radius: 50%; border: 12px solid var(--sky); }
  .brand-name { font-size: 64px; font-weight: 400; color: var(--sky); line-height: 1; margin-top: -26px; }

  .site-nav { position: absolute; left: 236px; top: 76px; width: 903px; height: 46px; border-bottom: 5px solid var(--sky); }
  .site-nav a {
    position: absolute; top: 0; height: 41px; line-height: 43px;
    font-size: 28px; font-weight: 700; color: var(--nav-ink); text-decoration: none;
    text-shadow: 2px 3px 3px rgba(0,0,0,0.35); transform: scaleX(0.92); transform-origin: left;
  }
  .site-nav .is-active { left: 330px; width: 110px; background: var(--sky); text-align: center; transform: none; }
  .site-nav .nav-about { left: 460px; }
  .site-nav .nav-pricing { left: 588px; }
  .site-nav .nav-signup { left: 723px; }
  .site-nav .nav-signin { left: 814px; }

  .hero {
    position: absolute; left: 58px; top: 155px; width: 1055px; height: 565px;
    background:
      linear-gradient(90deg, rgba(245,243,238,0.9) 0%, rgba(245,243,238,0.9) 17%, rgba(245,243,238,0) 19%, rgba(245,243,238,0) 78%, rgba(245,243,238,0.7) 82%, rgba(245,243,238,0.9) 100%),
      linear-gradient(180deg, var(--ceiling) 0%, #6d6558 16%, var(--wall-shade) 30%, var(--wall) 48%, var(--wall) 62%, #bdb7ac 76%, #4a4947 86%, var(--floor) 100%);
  }
  .hero-panel {
    position: absolute; left: 52px; top: 117px; width: 515px; height: 325px;
    background: var(--panel); border-radius: 16px; text-align: center;
  }
  .hero-title { margin-top: 12px; font-size: 39px; line-height: 46px; font-weight: 700; color: var(--ink); white-space: nowrap; }
  .hero-lede { margin-top: 18px; margin-left: -24px; font-size: 29px; font-weight: 700; color: var(--ink); line-height: 36px; }
  .hero-cta {
    position: absolute; left: 167px; top: 220px; width: 163px; height: 51px;
    border-radius: 26px; border: 3px solid var(--sky-deep);
    background: linear-gradient(180deg, var(--sky-light) 0%, var(--sky) 60%, var(--sky-deep) 100%);
    font-size: 22px; font-weight: 700; color: var(--ink); text-decoration: none;
    display: flex; align-items: center; justify-content: center;
  }

  .social-rail { position: absolute; left: 1128px; top: 157px; display: flex; flex-direction: column; gap: 5px; }
  .social-rail a { display: flex; align-items: center; justify-content: center; width: 56px; height: 57px; }
  .social-rail .tone-light { background: var(--social-light); }
  .social-rail .tone-dark { background: var(--social-dark); }
</style>
</head>
<body>
  <header>
    <a class="brand" href="http://www.vel-brook.co">
      <span class="brand-mark" aria-hidden="true"></span>
      <span class="brand-name">velbrook</span>
    </a>
    <nav class="site-nav">
      <a class="is-active" href="#home">Home</a>
      <a class="nav-about" href="#about">About Us</a>
      <a class="nav-pricing" href="#pricing">Pricing</a>
      <a class="nav-signup" href="#signup">Sign Up</a>
      <a class="nav-signin" href="#signin">Sign In</a>
    </nav>
  </header>

  <main class="hero" role="img" aria-label="Photograph of a bright white art gallery interior with a reception desk, track lighting and paintings on the walls">
    <section class="hero-panel">
      <h1 class="hero-title">Gallery Management Made Easy</h1>
      <p class="hero-lede">The simplest way to<br>manage your gallery in the cloud.</p>
      <a class="hero-cta" href="#about">Learn More</a>
    </section>
  </main>

  <aside class="social-rail" aria-label="Follow us">
    <a class="tone-light" href="#feed" aria-label="News feed">
      <svg width="30" height="30" viewBox="0 0 30 30" aria-hidden="true">
        <circle cx="6" cy="24" r="3.5" fill="#fff"/>
        <path d="M4 14a12 12 0 0 1 12 12" fill="none" stroke="#fff" stroke-width="3.5" stroke-linecap="round"/>
        <path d="M4 6a20 20 0 0 1 20 20" fill="none" stroke="#fff" stroke-width="3.5" stroke-linecap="round"/>
      </svg>
    </a>
    <a class="tone-dark" href="#social-1" aria-label="Social profile"></a>
    <a class="tone-light" href="#social-2" aria-label="Social profile"></a>
    <a class="tone-dark" href="#social-3" aria-label="Social profile"></a>
    <a class="tone-dark" href="#social-4" aria-label="Social profile"></a>
  </aside>
</body>
</html>
```